Olive oil labels

We are a small company of traditional products Olive oil, honey, pollen and various liqueurs and we would like to create an appealing and elegant label for our olive oil.
Use the Quiet Furrow logo. Design #: 7162085
Can or can not use the Castle.
Can be one or two labels (front and back)
Have to have all the text.
- Azeite Virgem Extra - In great prominence
- Azeite de categoria superior obtido diretamente de azeitonas, unicamente por processo mecânico.
- Edição Limitada
- produzido e embalado por DLM
- consumir preferência antes do fim de
- Lote
- Peso-Mogadouro | Trás-os-Montes
- Portugal
- sulcocalmo.lda@caixanova-mail.pt
(It has various sizes * 250ml (w4cmXh11cm)* 500ml (w9cmxh7) *750ml (w7xh13) *5L (w12cmxh14cm)

Target Market(s)

People with money expensive product but very good and in small quantity.

Industry/Entity Type

It Company

Font styles to use
Serif
Script

Colors

Designer to choose colors to be used in the design.

Requirements
Must have
• The castle of Mogadouro - attached image
Nice to have
• Maybe have written extra virgin olive oil in Portuguese " Azeite Virgem Extra" and English .
• Black label preference.

```html
<!DOCTYPE html>
<html lang="pt">
<head>
<meta charset="utf-8">
<title>Quiet Furrow — Azeite Virgem Extra, front and back labels</title>
<link rel="stylesheet" href="https://fonts.googleapis.com/css2?family=Josefin+Sans:wght@300;400;600&family=Cormorant+Garamond:wght@500;600&display=swap">
<style>
  :root {
    --backdrop: #eeeeee;
    --label-black: #1f1c1d;
    --gold: #c9a35c;
    --gold-soft: #b8975a;
    --gold-band: #cfae72;
    --ink-white: #ffffff;
    --ink-dark: #1b1818;
    --sans: "Josefin Sans", sans-serif;
    --serif: "Cormorant Garamond", serif;
  }
  * { box-sizing: border-box; margin: 0; padding: 0; }
  html, body { width: 1200px; height: 1000px; overflow: hidden; }
  body { background: var(--backdrop); position: relative; font-family: var(--sans); }

  /* Front label */
  .front-label {
    position: absolute; left: 190px; top: 90px;
    width: 320px; height: 810px;
    background: var(--label-black);
    border-radius: 160px 160px 0 0;
    text-align: center;
    color: var(--gold);
  }
  .brand { position: absolute; top: 70px; left: 0; right: 0; }
  .brand-dot {
    width: 60px; height: 60px; margin: 0 auto 14px;
    border-radius: 50%; background: var(--gold);
  }
  .brand-name {
    font-family: var(--serif); font-weight: 600;
    font-size: 26px; letter-spacing: 1px; color: var(--gold);
  }
  .front-title { position: absolute; top: 270px; left: 0; right: 0; }
  .front-title .azeite {
    font-weight: 600; font-size: 66px; color: var(--ink-white); line-height: 1;
  }
  .front-title .virgem {
    font-weight: 400; font-size: 30px; color: var(--ink-white); margin-top: 6px;
  }
  .front-title .edicao {
    font-weight: 300; font-size: 21px; color: var(--gold-soft); margin-top: 6px;
  }
  .castle-art {
    position: absolute; left: 40px; top: 470px; width: 240px; height: 170px;
    background: linear-gradient(180deg, #2a2524 0%, #3b3124 100%);
    border-bottom: 2px solid var(--gold);
  }
  .front-origin {
    position: absolute; top: 682px; left: 0; right: 0;
    font-weight: 300; font-size: 24px; color: var(--gold-soft);
  }
  .front-volume {
    position: absolute; top: 760px; left: 0; right: 0;
    font-weight: 300; font-size: 15px; color: var(--gold-soft);
  }

  /* Back label */
  .back-label {
    position: absolute; left: 620px; top: 220px;
    width: 420px; height: 580px;
    background: var(--label-black);
    color: var(--gold);
    text-align: center;
  }
  .back-frame { position: absolute; inset: 0; }
  .back-head { position: absolute; top: 56px; left: 0; right: 0; }
  .back-head .azeite { font-weight: 600; font-size: 46px; line-height: 1; }
  .back-head .virgem { font-weight: 400; font-size: 22px; margin-top: 4px; }
  .back-head .edicao { font-weight: 300; font-size: 14px; color: var(--gold-soft); margin-top: 4px; }
  .back-head .english {
    font-family: var(--serif); font-weight: 600; font-size: 21px; color: var(--gold); margin-top: 26px;
  }
  .quality-band {
    position: absolute; top: 246px; left: 0; right: 0; height: 80px;
    background: var(--gold-band); color: var(--ink-dark);
    font-weight: 600; font-size: 13.5px; line-height: 1.4;
    display: flex; align-items: center; justify-content: center;
  }
  .back-details { position: absolute; top: 374px; left: 0; right: 0; font-weight: 300; color: var(--gold-soft); }
  .back-details p { font-size: 12.5px; line-height: 1.4; }
  .back-details .producer { margin-bottom: 14px; }
  .lot-box {
    width: 170px; height: 26px; margin: 8px auto 18px;
    background: var(--ink-white);
  }
  .back-details .place { font-size: 11px; }
  .back-details .country { font-size: 15px; font-weight: 400; margin-top: 2px; }
</style>
</head>
<body>

<section class="front-label">
  <div class="brand">
    <div class="brand-dot"></div>
    <div class="brand-name">QUIET FURROW</div>
  </div>
  <div class="front-title">
    <div class="azeite">Azeite</div>
    <div class="virgem">Virgem Extra</div>
    <div class="edicao">Edição Limitada</div>
  </div>
  <div class="castle-art" role="img" aria-label="Gold line drawing of the Mogadouro castle tower and ruins"></div>
  <div class="front-origin">Portugal</div>
  <div class="front-volume">250ml</div>
</section>

<section class="back-label">
  <svg class="back-frame" width="420" height="580" viewBox="0 0 420 580" fill="none" stroke="#c9a35c" stroke-width="2">
    <polyline points="26,232 26,52 58,20 362,20 394,52 394,232"/>
    <polyline points="26,340 26,528 58,560 362,560 394,528 394,340"/>
  </svg>
  <div class="back-head">
    <div class="azeite">Azeite</div>
    <div class="virgem">Virgem Extra</div>
    <div class="edicao">Edição Limitada</div>
    <div class="english">Extra Virgin Olive Oil</div>
  </div>
  <div class="quality-band">
    <p>Azeite de categoria superior obtido<br>diretamente de azeitonas,<br>unicamente por processo mecânico</p>
  </div>
  <div class="back-details">
    <p class="producer">Produzido e embalado por DLM</p>
    <p>Consumir preferência antes<br>do fim de Lote</p>
    <div class="lot-box"></div>
    <p class="place">Peso-Mogadouro | Trás-os-Montes</p>
    <p class="country">Portugal</p>
  </div>
</section>

</body>
</html>
```